Business Cards using attached files

Please make new business cards using files attached. I would like something a little more updated possibly. Double sided.
I am wanting to make sure I can change the names and positions easily myself.

Target Market(s)

Automotive Repair

Industry/Entity Type

Automotive

Contact Information for Business Card

See attached files

Font styles to use
Serif

Colors
0054AA
0677BA
7BADD7
CADEEF
E8F1F8

Requirements
Must have
• Red white blue colors
Nice to have
• I'd like it slightly updated from our existing design. Double sided. I'd like to be able to change names and positions easily to have them printed.
Should not have
• I'm not sure

```html
<!DOCTYPE html>
<html lang="en">
<head>
<meta charset="utf-8">
<title>Harbor Auto &amp; Truck Center – Business Card</title>
<link rel="stylesheet" href="https://fonts.googleapis.com/css2?family=Arimo:wght@400;700&family=Tinos:wght@700&display=swap">
<style>
  :root {
    --red: #d3302f;
    --navy: #1f3a5f;
    --grey: #6b6b6b;
    --paper: #ffffff;
    --backdrop: #e6e6e6;
    --map-light: #f4f4f4;
    --map-dark: #d9dde3;
  }
  * { margin: 0; padding: 0; box-sizing: border-box; }
  html, body { width: 1200px; height: 802px; overflow: hidden; }
  body { background: var(--backdrop); position: relative; font-family: "Arimo", Arial, sans-serif; }

  .card {
    position: absolute; left: 290px; width: 620px; height: 354px;
    background: var(--paper); overflow: hidden;
    box-shadow: 0 4px 14px rgba(0,0,0,.18);
  }
  .card--front { top: 26px; }
  .card--back { top: 420px; font-family: "Tinos", "Times New Roman", serif; }

  /* Front */
  .tagline { position: absolute; left: 40px; top: 36px; color: var(--navy); font-weight: 700; font-size: 17px; line-height: 1.25; }
  .brand { position: absolute; left: 420px; top: 52px; color: var(--red); font-weight: 700; font-size: 38px; letter-spacing: 1px; }
  .person { position: absolute; left: 40px; top: 118px; }
  .person__name { color: var(--red); font-weight: 700; font-size: 25px; text-transform: uppercase; }
  .person__role { color: var(--grey); font-size: 16px; margin-top: 2px; }
  .person__address { color: var(--grey); font-size: 15px; line-height: 1.35; margin-top: 14px; }
  .contact { list-style: none; margin-top: 12px; color: var(--grey); font-size: 15px; }
  .contact li { display: flex; align-items: center; gap: 10px; line-height: 1.45; }
  .contact svg { width: 15px; height: 15px; fill: var(--red); flex: none; }
  .services { position: absolute; left: 372px; top: 172px; }
  .services__title { color: var(--red); font-size: 18px; text-transform: uppercase; margin-bottom: 6px; }
  .services__line { color: var(--grey); font-size: 15px; line-height: 1.5; }
  .dot { color: var(--red); }
  .edge { position: absolute; left: 0; bottom: 0; width: 620px; height: 16px; }

  /* Back */
  .map { position: absolute; left: 0; top: 0; width: 300px; height: 300px; background: linear-gradient(135deg, var(--map-light), var(--map-dark)); }
  .bands { position: absolute; left: 0; top: 0; width: 620px; height: 354px; }
  .pledge { position: absolute; left: 290px; top: 9px; color: #fff; font-size: 21px; }
  .features { position: absolute; left: 306px; top: 54px; list-style: none; color: var(--navy); font-size: 13.5px; line-height: 19.5px; }
  .features li::before { content: "•"; color: var(--red); margin-right: 5px; }
  .online { position: absolute; left: 418px; top: 218px; color: var(--navy); font-size: 23px; }
  .social { position: absolute; left: 470px; top: 252px; display: flex; gap: 7px; }
  .social span { width: 22px; height: 22px; border-radius: 50%; background: var(--red); }
  .shop { position: absolute; left: 24px; top: 296px; color: #fff; }
  .shop__name { font-size: 23px; }
  .shop__address { font-size: 15.5px; margin-top: 2px; }
  .website { position: absolute; right: 22px; bottom: 12px; color: #fff; font-size: 17px; }
</style>
</head>
<body>

<section class="card card--front" aria-label="Business card front">
  <p class="tagline">Family Owned &amp;<br>Operated Since 1991</p>
  <p class="brand">HARBOR</p>

  <div class="person">
    <p class="person__name">Daniel Corvino</p>
    <p class="person__role">General Manager</p>
    <p class="person__address">418 Route 25<br>Millbrook, NY 11790</p>
    <ul class="contact">
      <li><svg viewBox="0 0 24 24" aria-hidden="true"><path d="M6.6 10.8a15 15 0 0 0 6.6 6.6l2.2-2.2a1 1 0 0 1 1-.25 11.4 11.4 0 0 0 3.6.57 1 1 0 0 1 1 1V20a1 1 0 0 1-1 1A17 17 0 0 1 3 4a1 1 0 0 1 1-1h3.5a1 1 0 0 1 1 1c0 1.25.2 2.45.57 3.57a1 1 0 0 1-.25 1z"/></svg>(555) 014-2211</li>
      <li><svg viewBox="0 0 24 24" aria-hidden="true"><path d="M7 1h10a2 2 0 0 1 2 2v18a2 2 0 0 1-2 2H7a2 2 0 0 1-2-2V3a2 2 0 0 1 2-2zm0 4v13h10V5z"/></svg>(555) 016-7477</li>
      <li><svg viewBox="0 0 24 24" aria-hidden="true"><path d="M2 5h20v14H2zm2 2v.5l8 5 8-5V7z"/></svg>Dan@HarborAutoTruck.com</li>
    </ul>
  </div>

  <div class="services">
    <p class="services__title">Auto Service</p>
    <p class="services__line"><span class="dot">•</span> Inspections <span class="dot">•</span> Lube/Oil Service</p>
    <p class="services__line"><span class="dot">•</span> Diesel <span class="dot">•</span> Fleet <span class="dot">•</span> DOT <span class="dot">•</span> Truck <span class="dot">•</span> Trailer</p>
  </div>

  <svg class="edge" viewBox="0 0 620 16" preserveAspectRatio="none" aria-hidden="true">
    <polygon points="0,8 330,8 320,16 0,16" fill="var(--red)"/>
    <polygon points="340,0 620,0 620,16 326,16" fill="var(--navy)"/>
  </svg>
</section>

<section class="card card--back" aria-label="Business card back">
  <div class="map" role="img" aria-label="Simple street map showing how to reach the shop from nearby routes and the parkway"></div>

  <svg class="bands" viewBox="0 0 620 354" aria-hidden="true">
    <polygon points="300,0 620,0 620,42 280,42" fill="var(--red)"/>
    <polygon points="360,312 620,312 620,354 400,354" fill="var(--navy)"/>
    <polygon points="0,286 340,286 392,354 0,354" fill="var(--red)"/>
  </svg>

  <p class="pledge">We Stand Behind Our Service</p>

  <ul class="features">
    <li>Family Owned &amp; Operated</li>
    <li>Complimentary 2 year/24,000 mile warranty</li>
    <li>Free local pickup/dropoff service</li>
    <li>Experts In Domestic &amp; Import Service</li>
    <li>Master Certified Mechanics</li>
    <li>Diesel &amp; Fleet Services Available</li>
    <li>Honest, Knowledgeable, Trustworthy Service</li>
    <li>Top-Rated A+ Auto Repair Facility</li>
  </ul>

  <p class="online">Find Us Online:</p>
  <div class="social" aria-hidden="true"><span></span><span></span><span></span></div>

  <div class="shop">
    <p class="shop__name">Harbor Auto &amp; Truck Center</p>
    <p class="shop__address">418 Route 25, Millbrook, NY 11790</p>
  </div>
  <p class="website">www.HarborAutoTruck.com</p>
</section>

</body>
</html>
```